Introduction:
We are an Australia-based Cyber Security Penetration testing company seeking a website redesign to showcase our services, expertise, and experience. Our target audience includes businesses and organizations of all sizes who are seeking to secure their IT infrastructure against cyber threats. The purpose of the website redesign is to increase our online presence, generate leads, and establish our company as a trusted authority in the industry.
Objectives:
Create a professional and modern website that is easy to navigate and user-friendly.
Provide information about our company, services, and expertise.
Clearly display table of our 3 services: Bug Bounty as a Service, Penetration Testing and Code Review.
Generate leads through online contact forms and calls-to-action.
Optimize the website for search engines to increase visibility and traffic.
Website similar to: https://www.velmora.com.au/.
Target Audience:
Our target audience includes businesses and organizations of all sizes that require cybersecurity penetration testing services. These include:
Small and medium-sized enterprises (SMEs)
Australian Government agencies
Design Requirements:
Clean, modern, and professional design.
Use of colors that convey trust, reliability, and expertise (such as orange and grey).
Calls-to-action that encourage visitors to contact us or request a quote.
Integration with social media channels to increase engagement and brand awareness.
A blog section to showcase our thought leadership and expertise.
A news section to share updates about our company and the industry.
Content Requirements:
Home page that introduces our company and services and highlights our expertise.
About Us page that provides information about our company, team, and values.
Services page that lists our services and explains the benefits of each.
Case Studies page that showcases our previous work and success stories.
Contact Us page that includes a contact form, phone number, and email address.
Blog section with articles related to the cybersecurity industry and our services.
News section with updates about our company and the industry.

```html
<!DOCTYPE html>
<html lang="en">
<head>
<meta charset="utf-8">
<title>Emberveil — Cyber Security</title>
<link href="https://fonts.googleapis.com/css2?family=Montserrat:wght@600;700;800&family=Roboto:wght@400;500;700&display=swap" rel="stylesheet">
<style>
:root{
  --orange:#ee6a3e;
  --orange-deep:#e25a30;
  --grey:#4a4a4c;
  --ink:#2f2f31;
  --text:#555;
  --muted:#8d8d8d;
  --cream:#f5f1ee;
  --dark:#333336;
  --white:#fff;
  --navy:#0b2340;
  --blue:#1a5e9a;
}
*{margin:0;padding:0;box-sizing:border-box}
html,body{width:1200px;height:4218px;overflow:hidden}
body{position:relative;font-family:'Roboto',sans-serif;color:var(--text);background:var(--white)}
.abs{position:absolute}
.heading{font-family:'Montserrat',sans-serif;font-weight:800;color:var(--ink);text-align:center;font-size:36px;letter-spacing:0.5px}
.heading-rule{width:170px;height:2px;background:#999;margin:10px auto 0;position:relative}
.heading-rule::after{content:"";position:absolute;left:50%;top:-1px;width:58px;height:4px;margin-left:-29px;background:var(--orange)}
.btn{display:inline-block;background:var(--orange);color:var(--white);font-weight:700;font-size:15px;border-radius:30px;text-align:center;text-transform:uppercase}

/* top bar */
.topbar{top:0;left:0;width:1200px;height:37px;background:#f4f4f4}
.social{display:flex;gap:10px}
.social span{width:22px;height:22px;border-radius:50%;background:#fff;border:1px solid #ddd;display:block}
.social span.on{background:var(--orange);border-color:var(--orange)}
.topbar .social{position:absolute;left:111px;top:7px}
.contact-line{position:absolute;right:111px;top:10px;font-size:13px;color:var(--grey);display:flex;gap:16px;align-items:center}
.contact-line svg{vertical-align:-2px;margin-right:6px}

/* header */
.header{top:37px;left:0;width:1200px;height:100px;background:var(--white);z-index:3}
.logo-tab{position:absolute;left:84px;top:0;width:210px;height:132px;background:var(--white);clip-path:polygon(0 0,100% 0,100% 78%,86% 100%,14% 100%,0 78%)}
.brand{position:absolute;left:0;right:0;top:58px;text-align:center;font-family:'Montserrat',sans-serif;font-weight:700;font-size:28px;color:var(--orange)}
.brand-dot{position:absolute;left:82px;top:6px;width:46px;height:46px;border-radius:50%;border:5px solid var(--grey)}
.nav{position:absolute;left:423px;top:42px;display:flex;gap:26px;font-size:14px;font-weight:500;color:var(--ink)}
.nav .active{color:var(--orange)}
.header .btn{position:absolute;left:943px;top:28px;width:145px;height:48px;line-height:48px;font-size:14px}

/* hero */
.hero{top:137px;left:0;width:1200px;height:700px;background:radial-gradient(ellipse at 70% 30%,#1b6fae 0%,#0e3a66 45%,#07182e 100%)}
.hero-text{left:111px;top:175px;color:var(--white)}
.hero-text .kicker{font-family:'Montserrat',sans-serif;font-weight:700;font-size:24px}
.hero-text h1{font-family:'Montserrat',sans-serif;font-weight:800;font-size:46px;margin-top:4px}
.hero-text p{font-size:18px;font-weight:500;line-height:25px;margin-top:16px;width:440px}
.hero-text .btn{margin-top:27px;width:146px;height:46px;line-height:46px;font-size:14px}
.dots{left:1144px;top:255px;display:flex;flex-direction:column;gap:15px;align-items:center}
.dots i{width:6px;height:6px;border-radius:50%;background:#fff;display:block}
.dots i.cur{width:18px;height:18px;background:#bcc7d3;border:4px solid #e9eef3}
.curve{top:560px;left:0}

/* about */
.about{top:800px;left:0;width:1200px;height:546px;background:var(--cream)}
.about-mark{left:118px;top:128px;width:440px;height:320px;display:flex;align-items:center;justify-content:center;gap:18px;font-family:'Montserrat',sans-serif;font-weight:800;font-size:56px;color:var(--grey)}
.about-mark span.dot{width:56px;height:56px;border-radius:50%;background:var(--orange);display:block}
.about-copy{left:600px;top:100px;width:488px}
.about-copy h2{font-family:'Montserrat',sans-serif;font-weight:800;font-size:36px;color:var(--grey)}
.about-copy .bar{width:88px;height:4px;background:var(--orange);margin-top:4px}
.about-copy p{font-size:13.5px;line-height:26px;color:var(--muted);text-align:justify;margin-top:22px}
.about-copy p + p{margin-top:12px}
.about-copy .btn{margin-top:36px;width:146px;height:48px;line-height:48px}

/* services */
.services{top:1346px;left:0;width:1200px;height:766px}
.services .heading-wrap{position:absolute;top:100px;left:0;width:1200px}
.service{position:absolute;top:209px;width:308px;text-align:center}
.service .photo{width:308px;height:276px;border-top:8px solid var(--orange);border-radius:154px 154px 0 0;clip-path:circle(154px at 154px 154px)}
.service h3{font-size:14.5px;font-weight:700;color:var(--ink);margin-top:12px}
.service .mini{width:52px;height:2px;background:var(--orange);margin:6px auto 0}
.service p{font-size:12.5px;line-height:24px;color:var(--muted);margin-top:12px;padding:0 14px}
.service .btn{margin-top:14px;width:104px;height:32px;line-height:32px;font-size:10px}

/* expertise */
.expertise{top:2112px;left:0;width:1200px;height:641px;background:linear-gradient(135deg,#ea6337,#e1582f)}
.expertise .heading{color:var(--white)}
.expertise .heading-rule{background:rgba(255,255,255,.6)}
.expertise .heading-rule::after{background:var(--white)}
.card{position:absolute;width:475px;height:193px;border:2px solid rgba(255,255,255,.8);padding:28px 20px 0 102px;color:var(--white)}
.card.light{background:var(--white);border-color:var(--white);color:var(--grey)}
.card .icon{position:absolute;left:20px;top:28px}
.card h4{font-family:'Roboto',sans-serif;font-weight:700;font-size:16.5px;line-height:27px}
.card p{font-size:12.5px;line-height:24px;margin-top:12px;text-align:justify;opacity:.95}

/* blog */
.blog{top:2753px;left:0;width:1200px;height:629px}
.post{position:absolute;top:205px;width:310px;height:328px}
.post .photo{width:310px;height:205px}
.post .body{position:absolute;left:18px;top:182px;width:274px;height:146px;background:var(--white);box-shadow:0 6px 18px rgba(0,0,0,.12);text-align:center;padding-top:26px}
.post .body p{font-size:16px;line-height:25px;color:var(--ink)}
.post .body a{display:inline-block;margin-top:12px;font-size:13px;font-weight:700;color:var(--orange);text-decoration:underline}

/* contact */
.contact{top:3382px;left:0;width:1200px;height:836px;background:radial-gradient(ellipse at 20% 80%,#4a4a4e 0%,var(--dark) 60%)}
.contact .heading{color:var(--white)}
.info{position:absolute;left:131px;width:320px}
.info .pin{position:absolute;left:0;top:0;width:46px;height:46px;border-radius:50%;background:var(--white);display:flex;align-items:center;justify-content:center}
.info .txt{position:absolute;left:75px;top:0;color:var(--white)}
.info .txt b{display:block;font-size:15.5px;font-weight:700}
.info .txt span{display:block;font-size:13.5px;margin-top:5px}
.form{position:absolute;left:501px;top:187px;width:566px;height:335px;background:#f7ede8;border-radius:8px;padding:30px}
.field{position:absolute;background:var(--white);border-radius:3px;font-size:13px;color:#777;padding:14px 16px}
.form .btn{position:absolute;left:203px;top:259px;width:162px;height:48px;line-height:48px;font-size:14px}
.footer-rule{position:absolute;left:111px;width:978px;height:1px;background:rgba(255,255,255,.3)}
.footer-brand{position:absolute;left:0;width:1200px;top:604px;text-align:center;color:var(--white);font-family:'Montserrat',sans-serif;font-weight:700;font-size:27px}
.footer-brand .circ{display:block;width:44px;height:44px;border-radius:50%;border:4px solid var(--white);margin:0 auto 6px}
.footer-nav{position:absolute;left:0;width:1200px;top:707px;text-align:center;color:var(--white);font-size:16px;font-weight:700;word-spacing:2px}
.footer-nav i{font-style:normal;margin:0 19px}
.contact .social{position:absolute;left:533px;top:752px;gap:8px}
.contact .social span{width:26px;height:26px;background:transparent;border:2px solid var(--white)}
.contact .social span.on{background:var(--orange);border-color:var(--orange)}
.copyright{position:absolute;left:0;width:1200px;top:796px;text-align:center;color:var(--white);font-size:13px}
</style>
</head>
<body>

<div class="abs topbar">
  <div class="social"><span class="on"></span><span></span><span></span><span></span></div>
  <div class="contact-line">
    <span><svg width="12" height="12" viewBox="0 0 24 24"><path fill="#ee6a3e" d="M6.6 10.8a15 15 0 0 0 6.6 6.6l2.2-2.2c.3-.3.7-.4 1-.2 1.1.4 2.3.6 3.6.6.6 0 1 .4 1 1V20c0 .6-.4 1-1 1A17 17 0 0 1 3 4c0-.6.4-1 1-1h3.5c.6 0 1 .4 1 1 0 1.3.2 2.5.6 3.6.1.3 0 .7-.2 1z"/></svg>+1 (888) 888 8888</span>
    <span style="color:#bbb">|</span>
    <span><svg width="13" height="11" viewBox="0 0 24 18"><rect width="24" height="18" rx="2" fill="#ee6a3e"/><path d="M1 2l11 8 11-8" stroke="#fff" stroke-width="2" fill="none"/></svg>info@emberveil.com</span>
  </div>
</div>

<header class="abs header">
  <div class="logo-tab">
    <span class="brand-dot"></span>
    <div class="brand">Emberveil</div>
  </div>
  <nav class="nav"><span class="active">HOME</span><span>ABOUT US</span><span>SERVICES</span><span>CASE STUDIES</span><span>BLOG</span><span>NEWS</span></nav>
  <span class="btn">Contact Us</span>
</header>

<section class="abs hero" role="img" aria-label="Photo of hands typing on a laptop keyboard beneath a glowing digital security shield and network lines"></section>
<div class="abs hero-text">
  <div class="kicker">WELCOME TO</div>
  <h1>EMBERVEIL</h1>
  <p>Lorem ipsum dolor sit amet, consectetur adipiscing elit sed do eiusmod tempea.</p>
  <span class="btn">Get Started</span>
</div>
<div class="abs dots"><i></i><i class="cur"></i><i></i><i></i></div>

<section class="abs about">
  <div class="abs about-mark"><span class="dot"></span>Emberveil</div>
  <div class="abs about-copy">
    <h2>ABOUT US</h2>
    <div class="bar"></div>
    <p>Lorem ipsum dolor sit amet, consectetur adipiscing elit, sed do eiusmod tempor incididunt ut labore et dolore magna aliqua. Ut enim ad minim veniam, quis nostrud exercitation ullamco laboris nisi ut aliquip ex ea com modo conseque irure dolor in reprehenderitea.</p>
    <p>Aincididunt ut labore et dolore magna aliqua. Ut enim ad minim veniam, quis nostrud exercitation ullamco laboris nisi ut aliquip ex ea com modo conseque irure dolor in reprehenderitea.</p>
    <span class="btn">Learn More</span>
  </div>
</section>

<svg class="abs curve" width="1200" height="320" viewBox="0 560 1200 320">
  <path d="M0 660 Q600 940 1200 660 L1200 880 L0 880Z" fill="#f5f1ee"/>
  <path d="M0 676 Q600 954 1200 660" stroke="#ee6a3e" stroke-width="6" fill="none"/>
  <circle cx="600" cy="800" r="54" fill="#ee6a3e"/>
  <circle cx="600" cy="800" r="44" fill="#fff"/>
  <circle cx="600" cy="800" r="12" fill="none" stroke="#4a4a4c" stroke-width="3"/>
</svg>

<section class="abs services">
  <div class="heading-wrap"><h2 class="heading">OUR SERVICES</h2><div class="heading-rule"></div></div>
  <div class="service" style="left:111px">
    <div class="photo" role="img" aria-label="Photo of a hand holding a glowing padlock shield" style="background:radial-gradient(circle at 50% 45%,#8fb5d6,#2b4f78 55%,#13253d)"></div>
    <h3>BUG BOUNTY</h3><div class="mini"></div>
    <p>Sed ut perspiciatis unde omnis iste natus err or sit voluptatem accusantium doloremque laudantium totam remea.</p>
    <span class="btn">Learn More</span>
  </div>
  <div class="service" style="left:446px">
    <div class="photo" role="img" aria-label="Photo of two colleagues reviewing a laptop in a server room" style="background:linear-gradient(160deg,#3d4e63,#1d2633 60%,#c9a88a)"></div>
    <h3>PENETRATION TESTING</h3><div class="mini"></div>
    <p>Sed ut perspiciatis unde omnis iste natus err or sit voluptatem accusantium doloremque laudantium totam remea.</p>
    <span class="btn">Learn More</span>
  </div>
  <div class="service" style="left:781px">
    <div class="photo" role="img" aria-label="Photo of a team reviewing code on screens" style="background:linear-gradient(160deg,#6d86a8,#2c3c55 55%,#1a2434)"></div>
    <h3>CODE REVIEW</h3><div class="mini"></div>
    <p>Sed ut perspiciatis unde omnis iste natus err or sit voluptatem accusantium doloremque laudantium totam remea.</p>
    <span class="btn">Learn More</span>
  </div>
</section>

<section class="abs expertise">
  <div style="position:absolute;top:76px;left:0;width:1200px"><h2 class="heading">OUR EXPERTISE</h2><div class="heading-rule"></div></div>
  <div class="card" style="left:111px;top:158px">
    <svg class="icon" width="44" height="48" viewBox="0 0 44 48"><circle cx="22" cy="18" r="14" fill="#fff"/><rect x="15" y="34" width="14" height="8" rx="2" fill="#fff"/></svg>
    <h4>LOREM IPSUM DOLOR SIT AMET CON SECTETUR ADIPISCING</h4>
    <p>Sed ut perspiciatis unde omnis iste natus error sit volupta tem accusantium doloremque laudantium, totam rem aperiam eaque ipsa quae ab illo.</p>
  </div>
  <div class="card light" style="left:612px;top:158px">
    <svg class="icon" width="50" height="50" viewBox="0 0 50 50"><circle cx="25" cy="25" r="20" fill="none" stroke="#ee6a3e" stroke-width="4"/><path d="M14 27l8 7 14-15" stroke="#ee6a3e" stroke-width="4" fill="none"/></svg>
    <h4>LOREM IPSUM DOLOR SIT AMET CON SECTETUR ADIPISCING</h4>
    <p>Sed ut perspiciatis unde omnis iste natus error sit volupta tem accusantium doloremque laudantium, totam rem aperiam eaque ipsa quae ab illo.</p>
  </div>
  <div class="card" style="left:111px;top:380px">
    <svg class="icon" width="56" height="52" viewBox="0 0 56 52"><circle cx="28" cy="26" r="8" fill="#fff"/><circle cx="9" cy="9" r="6" fill="none" stroke="#fff" stroke-width="3"/><circle cx="47" cy="9" r="6" fill="none" stroke="#fff" stroke-width="3"/><circle cx="9" cy="43" r="6" fill="none" stroke="#fff" stroke-width="3"/><circle cx="47" cy="43" r="6" fill="none" stroke="#fff" stroke-width="3"/><path d="M13 13l9 8M43 13l-9 8M13 39l9-8M43 39l-9-8" stroke="#fff" stroke-width="2"/></svg>
    <h4>LOREM IPSUM DOLOR SIT AMET CON SECTETUR ADIPISCING</h4>
    <p>Sed ut perspiciatis unde omnis iste natus error sit volupta tem accusantium doloremque laudantium, totam rem aperiam eaque ipsa quae ab illo.</p>
  </div>
  <div class="card" style="left:612px;top:380px">
    <svg class="icon" width="52" height="52" viewBox="0 0 52 52"><circle cx="26" cy="26" r="20" fill="none" stroke="#fff" stroke-width="4" stroke-dasharray="10 5"/><circle cx="26" cy="26" r="8" fill="#fff"/></svg>
    <h4>LOREM IPSUM DOLOR SIT AMET CON SECTETUR ADIPISCING</h4>
    <p>Sed ut perspiciatis unde omnis iste natus error sit volupta tem accusantium doloremque laudantium, totam rem aperiam eaque ipsa quae ab illo.</p>
  </div>
</section>

<section class="abs blog">
  <div style="position:absolute;top:100px;left:0;width:1200px"><h2 class="heading">LATEST BLOG POST</h2><div class="heading-rule"></div></div>
  <article class="post" style="left:111px">
    <div class="photo" role="img" aria-label="Photo of a person at a laptop showing a padlock on screen" style="background:linear-gradient(150deg,#2f5a8c,#0f2542)"></div>
    <div class="body"><p>Lorem ipsum dolor sit amet<br>consectetur adipiscing<br>elit sesumd do</p><a>READ MORE</a></div>
  </article>
  <article class="post" style="left:445px">
    <div class="photo" role="img" aria-label="Photo of a developer pointing at code on a monitor" style="background:linear-gradient(150deg,#6e5a4c,#2a2626 60%,#8a8f96)"></div>
    <div class="body"><p>Lorem ipsum dolor sit amet<br>consectetur adipiscing<br>elit sesumd do</p><a>READ MORE</a></div>
  </article>
  <article class="post" style="left:778px">
    <div class="photo" role="img" aria-label="Photo of an analyst at multiple monitors in a security operations room" style="background:linear-gradient(150deg,#4d7fb8,#17365e 60%,#0c1c33)"></div>
    <div class="body"><p>Lorem ipsum dolor sit amet<br>consectetur adipiscing<br>elit sesumd do</p><a>READ MORE</a></div>
  </article>
</section>

<footer class="abs contact">
  <div style="position:absolute;top:78px;left:0;width:1200px"><h2 class="heading">GET IIN TOUCH</h2></div>
  <div class="info" style="top:256px">
    <div class="pin"><svg width="16" height="20" viewBox="0 0 16 20"><path d="M8 0a8 8 0 0 0-8 8c0 6 8 12 8 12s8-6 8-12a8 8 0 0 0-8-8z" fill="#ee6a3e"/><circle cx="8" cy="8" r="3" fill="#fff"/></svg></div>
    <div class="txt"><b>LOCATIONS:</b><span>465, Lorum Ipsum Dol, Australia</span></div>
  </div>
  <div class="info" style="top:331px">
    <div class="pin"><svg width="18" height="18" viewBox="0 0 24 24"><path fill="#ee6a3e" d="M6.6 10.8a15 15 0 0 0 6.6 6.6l2.2-2.2c.3-.3.7-.4 1-.2 1.1.4 2.3.6 3.6.6.6 0 1 .4 1 1V20c0 .6-.4 1-1 1A17 17 0 0 1 3 4c0-.6.4-1 1-1h3.5c.6 0 1 .4 1 1 0 1.3.2 2.5.6 3.6.1.3 0 .7-.2 1z"/></svg></div>
    <div class="txt"><b>PHONE:</b><span>+1 (888 ) 888 8888</span></div>
  </div>
  <div class="info" style="top:406px">
    <div class="pin"><svg width="18" height="14" viewBox="0 0 24 18"><rect width="24" height="18" rx="2" fill="#ee6a3e"/><path d="M1 2l11 8 11-8" stroke="#fff" stroke-width="2" fill="none"/></svg></div>
    <div class="txt"><b>EMAIL:</b><span>info@emberveil.com</span></div>
  </div>
  <form class="form">
    <div class="field" style="left:30px;top:30px;width:250px;height:48px">First Name</div>
    <div class="field" style="left:287px;top:30px;width:250px;height:48px">Last Name</div>
    <div class="field" style="left:30px;top:90px;width:250px;height:48px">Email</div>
    <div class="field" style="left:287px;top:90px;width:250px;height:48px">Phone</div>
    <div class="field" style="left:30px;top:150px;width:507px;height:95px">Message</div>
    <span class="btn">Send Message</span>
  </form>
  <div class="footer-rule" style="top:576px"></div>
  <div class="footer-brand"><span class="circ"></span>Emberveil</div>
  <div class="footer-nav">HOME<i>/</i>WHO WE ARE<i>/</i>SERVICES<i>/</i>CASE STUDIES<i>/</i>BLOG<i>/</i>NEWS<i>/</i>CONTACT US</div>
  <div class="footer-rule" style="top:740px"></div>
  <div class="social"><span class="on"></span><span></span><span></span><span></span></div>
  <div class="copyright">© 2023 EMBERVEIL &nbsp;|&nbsp; All Rights Reserved</div>
</footer>

</body>
</html>
```